Brantel Construction Core Values Wall Design

Core Values Wall Design for our Wall, I’m not exactly sure visually what we would want it to look like. Maybe some acrylic stand offs that could go on brick? If that’s a possibility. That’s where we have the most space in the office. But we could do other locations too.

These are our core values
• Safety
• Integrity
• Quality
• Client-Focused Solutions
• Continuous Improvement
• Positive Culture and Stewardship

Our vision/mission statement is Steady Craft Built.

```html
<!DOCTYPE html>
<html lang="en">
<head>
<meta charset="UTF-8">
<title>Brantel Construction — Core Values Wall</title>
<link rel="stylesheet" href="https://fonts.googleapis.com/css2?family=Archivo+Black&family=Barlow+Semi+Condensed:wght@600&family=League+Spartan:wght@600;700&family=Montserrat:wght@500&family=Oswald:wght@600&display=swap">
<style>
  :root {
    --wall: #e5e6d8;
    --navy: #0f5284;
    --red: #d42027;
    --cream: #ecebdc;
  }
  html, body {
    margin: 0;
    padding: 0;
    width: 1200px;
    height: 800px;
    overflow: hidden;
    background: var(--wall);
  }
  .values-wall { display: block; width: 1200px; height: 800px; }
  .navy-fill { fill: var(--navy); }
  .red-fill { fill: var(--red); }
  .light-fill { fill: var(--cream); }
  .tag-label { font-family: "Montserrat", sans-serif; font-weight: 500; }
  .brand-name { font-family: "League Spartan", sans-serif; font-weight: 700; }
  .headline { font-family: "League Spartan", sans-serif; font-weight: 700; }
  .value-condensed { font-family: "Barlow Semi Condensed", sans-serif; font-weight: 600; }
  .value-script { font-family: "League Spartan", sans-serif; font-weight: 600; }
  .value-heavy { font-family: "Archivo Black", sans-serif; }
  .value-band { font-family: "Oswald", sans-serif; font-weight: 600; }
</style>
</head>
<body>
<svg class="values-wall" viewBox="0 0 1200 800" xmlns="http://www.w3.org/2000/svg" role="img" aria-label="Brantel Construction core values wall">
  <g transform="translate(279,168)">
    <!-- mission / vision tag -->
    <g class="mission-tag">
      <polygon class="red-fill" points="0,0 206,0 197,17 206,34 0,34"/>
      <circle cx="16" cy="18" r="8" fill="none" stroke="var(--cream)" stroke-width="2.5"/>
      <circle cx="16" cy="18" r="3" class="light-fill"/>
      <text class="tag-label light-fill" x="30" y="25" font-size="20" textLength="150" lengthAdjust="spacingAndGlyphs">mission/vision</text>
    </g>

    <!-- company name -->
    <g class="brand-mark">
      <rect class="navy-fill" x="473" y="17" width="12" height="12"/>
      <text class="brand-name navy-fill" x="631" y="29" font-size="16" text-anchor="end" textLength="140" lengthAdjust="spacingAndGlyphs">BRANTEL CONSTRUCTION</text>
    </g>

    <!-- vision statement -->
    <text class="headline navy-fill" x="0" y="102" font-size="86" textLength="631" lengthAdjust="spacingAndGlyphs">Steady Craft Built</text>
    <rect class="navy-fill" x="0" y="111" width="631" height="2.5"/>

    <!-- client-focused solutions -->
    <text class="value-condensed red-fill" x="0" y="159" font-size="46" textLength="327" lengthAdjust="spacingAndGlyphs">CLIENT-FOCUSED</text>
    <text class="value-condensed red-fill" x="0" y="209" font-size="46" textLength="225" lengthAdjust="spacingAndGlyphs">SOLUTIONS</text>
    <path class="navy-fill" d="M250 177h5l-12 30h-5zM260 177h5l-12 30h-5zM270 177h5l-12 30h-5zM280 177h5l-12 30h-5zM290 177h5l-12 30h-5zM300 177h5l-12 30h-5zM310 177h5l-12 30h-5zM320 177h5l-12 30h-5z"/>

    <!-- core values tag -->
    <g class="core-values-tag">
      <polygon class="navy-fill" points="334,126 564,126 556,142.5 564,159 334,159 342,142.5"/>
      <text class="tag-label light-fill" x="449" y="153" font-size="31" text-anchor="middle" textLength="190" lengthAdjust="spacingAndGlyphs">core values</text>
    </g>

    <!-- safety -->
    <text class="value-script navy-fill" x="337" y="208" font-size="78" textLength="180" lengthAdjust="spacingAndGlyphs">safety</text>
    <g class="safety-shield">
      <path class="red-fill" d="M541 171L561 178V192C561 203 551 210 541 214C531 210 521 203 521 192V178Z"/>
      <path d="M532 192l6 6l12-12" fill="none" stroke="var(--cream)" stroke-width="4" stroke-linecap="round" stroke-linejoin="round"/>
    </g>

    <!-- integrity -->
    <text class="value-heavy navy-fill" x="0" y="294" font-size="96" textLength="555" lengthAdjust="spacingAndGlyphs">INTEGRITY</text>

    <!-- continuous improvement band -->
    <rect class="red-fill" x="0" y="304" width="557" height="71"/>
    <text class="value-band light-fill" x="6" y="366" font-size="70" textLength="545" lengthAdjust="spacingAndGlyphs">CONTINUOUS IMPROVEMENT</text>

    <!-- positive culture and stewardship -->
    <text class="value-heavy navy-fill" x="0" y="416" font-size="40" textLength="260" lengthAdjust="spacingAndGlyphs">POSITIVE</text>
    <text class="value-heavy navy-fill" x="303" y="416" font-size="40" textLength="255" lengthAdjust="spacingAndGlyphs">CULTURE</text>
    <text class="value-heavy navy-fill" x="0" y="451" font-size="40" textLength="120" lengthAdjust="spacingAndGlyphs">AND</text>
    <text class="value-heavy navy-fill" x="148" y="451" font-size="40" textLength="410" lengthAdjust="spacingAndGlyphs">STEWARDSHIP</text>

    <!-- quality, vertical -->
    <text class="value-heavy red-fill" transform="translate(568,126) rotate(90)" x="0" y="0" font-size="88" textLength="327" lengthAdjust="spacingAndGlyphs">QUALITY</text>
  </g>
</svg>
</body>
</html>
```